All-natural soap packaging design for new company

The box type has been selected, we just need artwork for each of our 10 products. I'd like the same look to each, the idea is just to switch out the name and ingredient label on each. The dimensions are 3.5"x3.75"x1.25". The colors in the uploaded pictures with product titles are not mandatory. I'd like to keep the font on the packaging (Rubik) as it is the same as the website.

Target Market(s)

Health & Beauty, people looking for natural or organic products

Industry/Entity Type

It Company

Colors

Designer to choose colors to be used in the design.

Requirements
Must have
• Design must be clean and relatively simple. Slightly different look for each of the 10 products. Audience is people looking for all-natural products.

```html
<!DOCTYPE html>
<html lang="en">
<head>
<meta charset="utf-8">
<title>Lavender + Witch Hazel – Soap Box Artwork</title>
<link href="https://fonts.googleapis.com/css2?family=Rubik:ital,wght@0,500;0,700;1,700&display=swap" rel="stylesheet">
<style>
  :root {
    --backdrop: #c4aabf;
    --panel-pink: #f4dff0;
    --foam-light: #f2d4ec;
    --foam-mid: #d98ecd;
    --purple: #c06cb6;
    --purple-deep: #a44c9c;
    --trim-blue: #1f6db5;
    --trim-blue-dark: #17558f;
    --fold-line: #3a2f3a;
    --cut-line: #e0535a;
    --white: #ffffff;
    --brand-grey: #5a5a5a;
    --lavender: #7b5ab0;
    --leaf: #8fb56a;
  }
  * { box-sizing: border-box; margin: 0; padding: 0; }
  html, body { width: 1200px; height: 613px; overflow: hidden; }
  body {
    background: var(--backdrop);
    font-family: "Rubik", Arial, sans-serif;
    position: relative;
  }

  /* ---------- Dieline ---------- */
  .dieline {
    position: absolute;
    left: 76px; top: 26px;
    width: 214px; height: 562px;
    border: 1px solid var(--cut-line);
    border-top-left-radius: 16px;
    border-top-right-radius: 16px;
    background: var(--trim-blue);
    overflow: hidden;
  }
  .dieline .inner {
    position: absolute;
    left: 6px; right: 6px; top: 0; bottom: 8px;
  }
  .dieline .flap {
    position: absolute; left: 0; right: 0; top: 0; height: 26px;
    background: var(--panel-pink);
    border-top-left-radius: 14px; border-top-right-radius: 14px;
    border-bottom: 1px solid var(--fold-line);
  }
  .dieline .flap::before {
    content: ""; position: absolute; left: 4px; right: 4px; top: 6px; bottom: -1px;
    border: 1px solid var(--fold-line); border-bottom: none;
    border-top-left-radius: 12px; border-top-right-radius: 12px;
  }
  .dieline .plain-panel {
    position: absolute; left: 0; right: 0;
    background: var(--panel-pink);
    border-bottom: 1px solid var(--fold-line);
  }
  .panel-back-top { top: 26px; height: 70px; }
  .panel-bottom { top: 292px; height: 68px; }
  .panel-back { top: 360px; height: 194px; }

  /* ---------- Front face (shared) ---------- */
  .front {
    position: absolute;
    overflow: hidden;
    background: linear-gradient(180deg, var(--purple) 0%, var(--purple-deep) 100%);
  }
  .front .foam {
    position: absolute; left: 0; right: 0; top: 0;
    background: linear-gradient(180deg, var(--foam-light) 0%, var(--foam-mid) 70%, rgba(217,142,205,0) 100%);
  }
  .front .brand-tab {
    position: absolute; top: 0;
    background: var(--white);
    border: 2px solid var(--trim-blue);
    border-top: none;
    border-bottom-left-radius: 12px; border-bottom-right-radius: 12px;
    display: flex; flex-direction: column; align-items: center; justify-content: flex-end;
  }
  .brand-tab .brand-mark {
    border: 2px solid var(--trim-blue);
  }
  .brand-tab .brand-name {
    font-weight: 500; color: var(--brand-grey);
    text-transform: uppercase; white-space: nowrap;
  }
  .front .product-title {
    position: absolute; left: 0; right: 0;
    text-align: center; color: var(--white);
    font-weight: 700; text-transform: uppercase;
    line-height: 1;
  }
  .product-title .line-main { display: block; }
  .product-title .line-sub { display: block; font-weight: 500; }
  .front .ingredient-art {
    position: absolute;
    border-radius: 50%;
    border: 3px solid var(--trim-blue);
    background: radial-gradient(ellipse at 50% 40%, var(--lavender) 0%, #a98bd0 28%, var(--white) 55%, #e9f1e2 75%, var(--leaf) 100%);
  }
  .front .side-trim {
    position: absolute; top: 0; bottom: 0; background: var(--trim-blue);
  }

  /* dieline front sizing */
  .front-small { left: 0; right: 0; top: 96px; height: 196px; border-bottom: 1px solid var(--fold-line); border-top: 1px solid var(--fold-line); }
  .front-small .foam { height: 70px; }
  .front-small .brand-tab { left: 88px; width: 46px; height: 52px; padding-bottom: 4px; gap: 3px; border-width: 1.5px; }
  .front-small .brand-mark { width: 28px; height: 28px; border-width: 1.5px; }
  .front-small .brand-name { font-size: 4px; }
  .front-small .product-title { top: 74px; text-shadow: 1.5px 1.5px 0 var(--trim-blue-dark); }
  .front-small .line-main { font-size: 29px; }
  .front-small .line-sub { font-size: 19px; }
  .front-small .ingredient-art { left: 60px; top: 140px; width: 96px; height: 96px; border-width: 2px; }

  /* presentation front sizing */
  .front-large { left: 420px; top: 72px; width: 520px; height: 472px; }
  .front-large .side-trim { left: 0; width: 14px; }
  .front-large .side-trim.right { left: auto; right: 0; }
  .front-large .foam { height: 175px; }
  .front-large .brand-tab { left: 212px; width: 96px; height: 124px; padding-bottom: 8px; gap: 6px; }
  .front-large .brand-mark { width: 62px; height: 72px; }
  .front-large .brand-name { font-size: 8.5px; }
  .front-large .product-title { top: 180px; left: 18px; text-shadow: 3px 3px 0 var(--trim-blue-dark); }
  .front-large .line-main { font-size: 74px; letter-spacing: 1px; }
  .front-large .line-sub { font-size: 52px; margin-top: 4px; }
  .front-large .ingredient-art { left: 130px; top: 345px; width: 272px; height: 272px; }
</style>
</head>
<body>

  <section class="dieline" aria-label="Flat box dieline">
    <div class="inner">
      <div class="flap"></div>
      <div class="plain-panel panel-back-top"></div>
      <div class="front front-small">
        <div class="foam" role="img" aria-label="Soap foam bubbles photo"></div>
        <div class="brand-tab">
          <div class="brand-mark"></div>
          <span class="brand-name">Alder Soap Co.</span>
        </div>
        <h2 class="product-title">
          <span class="line-main">Lavender +</span>
          <span class="line-sub">Witch Hazel</span>
        </h2>
        <div class="ingredient-art" role="img" aria-label="Lavender sprigs illustration"></div>
      </div>
      <div class="plain-panel panel-bottom"></div>
      <div class="plain-panel panel-back"></div>
    </div>
  </section>

  <section class="front front-large" aria-label="Box front panel">
    <div class="foam" role="img" aria-label="Soap foam bubbles photo"></div>
    <div class="side-trim"></div>
    <div class="side-trim right"></div>
    <div class="brand-tab">
      <div class="brand-mark"></div>
      <span class="brand-name">Alder Soap Co.</span>
    </div>
    <h1 class="product-title">
      <span class="line-main">Lavender +</span>
      <span class="line-sub">Witch Hazel</span>
    </h1>
    <div class="ingredient-art" role="img" aria-label="Lavender sprigs with green leaves illustration"></div>
  </section>

</body>
</html>
```